Typing Service Business Card Design

Need a new business card design for new logo update. The Ledger Scribes is an outsourced typing service. We type audio / voice files into word documents. We are a professional service that is recognised in the industry over the past 15 years and have a strong connection to our brand. The final design should be professional, simple, yet effective.

Corinna Waldrop
Director

corinna@lsx.com.au
www.theledgerscribes.com.au

```html
<!DOCTYPE html>
<html lang="en">
<head>
<meta charset="utf-8">
<title>The Ledger Scribes – Business Card</title>
<link rel="stylesheet" href="https://fonts.googleapis.com/css2?family=Arimo:wght@400;700&family=Open+Sans:wght@400;600&display=swap">
<style>
  :root {
    --brand-pink: #d9449f;
    --card-white: #ffffff;
    --ink: #1a1a1a;
    --backdrop: #34302d;
  }
  * { box-sizing: border-box; margin: 0; padding: 0; }
  html, body {
    width: 1200px;
    height: 844px;
    overflow: hidden;
    background: var(--backdrop);
  }
  .stage {
    position: relative;
    width: 1200px;
    height: 844px;
    display: flex;
    align-items: center;
    justify-content: center;
    gap: 40px;
  }
  .card {
    position: relative;
    width: 525px;
    height: 300px;
    border-radius: 2px;
    overflow: hidden;
  }
  .card--front { background: var(--card-white); }
  .card--back { background: var(--brand-pink); }

  .brand {
    position: absolute;
    right: 30px;
    top: 40px;
    text-align: right;
    font-family: "Arimo", Arial, sans-serif;
  }
  .brand__name {
    display: flex;
    align-items: center;
    justify-content: flex-end;
    gap: 8px;
    color: var(--brand-pink);
    font-weight: 700;
    font-size: 25px;
    letter-spacing: -0.3px;
  }
  .brand__dot {
    width: 12px;
    height: 12px;
    border-radius: 50%;
    background: var(--brand-pink);
  }
  .brand__tagline {
    margin-top: 4px;
    font-size: 16px;
    color: var(--ink);
  }

  .contact {
    position: absolute;
    left: 30px;
    bottom: 32px;
    font-family: "Open Sans", Arial, sans-serif;
    color: var(--ink);
  }
  .contact__name {
    color: var(--brand-pink);
    font-weight: 600;
    font-size: 19px;
  }
  .contact__role {
    font-size: 13px;
    margin-bottom: 14px;
  }
  .contact__line {
    display: flex;
    align-items: center;
    gap: 9px;
    font-size: 14px;
    line-height: 22px;
  }
  .contact__icon { width: 11px; height: 11px; flex: none; }

  .back-brand {
    position: absolute;
    right: 34px;
    top: 150px;
    text-align: right;
    font-family: "Arimo", Arial, sans-serif;
    color: var(--card-white);
  }
  .back-brand__name {
    font-weight: 700;
    font-size: 24px;
    letter-spacing: 0.3px;
  }
  .back-brand__tagline {
    margin-top: 8px;
    font-size: 16px;
    opacity: 0.85;
  }
</style>
</head>
<body>
  <main class="stage">
    <section class="card card--front" aria-label="Business card front">
      <div class="brand">
        <div class="brand__name"><span class="brand__dot"></span>The Ledger Scribes</div>
        <div class="brand__tagline">Spoken in. Typed out.</div>
      </div>
      <div class="contact">
        <div class="contact__name">Corinna Waldrop</div>
        <div class="contact__role">Director</div>
        <div class="contact__line">
          <svg class="contact__icon" viewBox="0 0 12 12" aria-hidden="true">
            <rect x="0.5" y="2" width="11" height="8" fill="#d9449f"/>
            <path d="M0.8 2.4 L6 6.6 L11.2 2.4" fill="none" stroke="#fff" stroke-width="1.1"/>
          </svg>
          <span>corinna@lsx.com.au</span>
        </div>
        <div class="contact__line">
          <svg class="contact__icon" viewBox="0 0 12 12" aria-hidden="true">
            <g fill="none" stroke="#d9449f" stroke-width="1.6" stroke-linecap="round">
              <path d="M5 7 L7 5"/>
              <path d="M4.2 5.6 L2.6 7.2 a1.8 1.8 0 0 0 2.5 2.5 L6.7 8.1"/>
              <path d="M7.8 6.4 L9.4 4.8 a1.8 1.8 0 0 0 -2.5 -2.5 L5.3 3.9"/>
            </g>
          </svg>
          <span>www.theledgerscribes.com.au</span>
        </div>
      </div>
    </section>

    <section class="card card--back" aria-label="Business card back">
      <div class="back-brand">
        <div class="back-brand__name">The Ledger Scribes</div>
        <div class="back-brand__tagline">Spoken in. Typed out.</div>
      </div>
    </section>
  </main>
</body>
</html>
```